Lanternfield Prose Studio (LPStudio.net)

We need a Wordpress-based site designed for a client who provides writing and editing services for the IT industry. We have a wireframe complete for the homepage, but need all internal pages designed (based on homepage wireframe) and the entire site coded for WP.

Internal pages include: "Our Work" (with samples & testimonials); "Capabilities" (with sections to address "strategy", "coaching", "writing" and "editing"); "About Us"; and a Contact page.

Will provide all copywriting, writing samples, testimonials, and client logos.

We completely realize/acknowledge the subject matter is visually BORING! Anything at all that can be done to make it look visually appealing would be *great*! Stock photography is fine.

Please feel free to ask any questions whatsoever. Thanks for your time!

```html
<!DOCTYPE html>
<html lang="en">
<head>
<meta charset="utf-8">
<title>Lanternfield Prose Studio</title>
<link rel="stylesheet" href="https://fonts.googleapis.com/css2?family=Montserrat:wght@400;500;600;700;800&family=Outfit:wght@300;400;500;600&display=swap">
<style>
:root{
  --navy:#0f1330;
  --green:#3cc13b;
  --blue:#1473f0;
  --blue-dark:#1d4fa0;
  --blue-light:#2a9be8;
  --ink:#1b1c2c;
  --muted:#3a3b48;
  --slate:#2b2a3e;
  --steel:#8b8c99;
  --paper:#ffffff;
  --footer:#f2f3f8;
  --line:#d9dbe3;
}
*{box-sizing:border-box;margin:0;padding:0}
html,body{width:1200px;height:2754px;overflow:hidden;background:var(--paper)}
body{font-family:"Montserrat",sans-serif;color:var(--ink);position:relative}
.page{position:relative;width:1200px;height:2754px}

/* header */
.site-header{position:absolute;left:0;top:0;width:1200px;height:62px;background:var(--paper);z-index:5}
.brand-panel{position:absolute;left:0;top:0;width:406px;height:62px;background:var(--navy)}
.brand{position:absolute;font-family:"Montserrat",sans-serif;font-weight:800;font-size:19px;letter-spacing:-.2px;white-space:nowrap}
.brand .u{position:relative}
.brand .u::after{content:"";position:absolute;left:0;right:0;bottom:-6px;height:2px;background:var(--blue)}
.site-header .brand{left:93px;top:18px;color:#fff}
.nav a{position:absolute;top:26px;font-size:10px;font-weight:700;color:var(--ink);text-decoration:none;letter-spacing:.2px}
.nav a.active{color:var(--green)}
.btn{position:absolute;display:flex;align-items:center;justify-content:center;border-radius:16px;color:#fff;font-size:9.5px;font-weight:700;letter-spacing:.2px;text-decoration:none;white-space:nowrap}
.btn-blue{background:var(--blue)}
.btn-green{background:var(--green)}

/* hero */
.hero{position:absolute;left:0;top:0;width:1200px;height:668px;background:var(--navy);overflow:hidden}
.hero-photo{position:absolute;left:319px;top:62px;width:881px;height:606px;background:linear-gradient(120deg,#3d4f56 0%,#6f8a86 35%,#9aa7a3 60%,#4a4e52 100%)}
.hero-title{position:absolute;left:93px;top:183px;width:760px;font-family:"Outfit",sans-serif;font-weight:500;font-size:47px;line-height:57px;color:#fff;white-space:nowrap}
.hero-dots{position:absolute;left:1094px;top:276px}
.hero-dots span{display:block;width:11px;height:11px;border:1.5px solid #fff;border-radius:50%;margin-bottom:10.5px}
.hero-dots span.on{background:radial-gradient(circle,#fff 2px,transparent 2.5px)}
.hero-wave{position:absolute;left:0;top:0}

/* intro + services */
.section-title{position:absolute;left:0;width:1200px;text-align:center;font-family:"Outfit",sans-serif;font-weight:500;font-size:31px;line-height:40px;color:var(--ink)}
.service{position:absolute;top:811px;width:234px;height:312px;background:#fff;box-shadow:0 2px 8px rgba(20,25,60,.1)}
.service .pic{width:234px;height:157px}
.service .tag{position:absolute;left:0;top:141px;width:147px;height:31px;padding-left:18px;color:#fff;font-family:"Outfit",sans-serif;font-size:16px;line-height:31px;clip-path:polygon(0 0,120px 0,147px 100%,0 100%)}
.service p{position:absolute;left:18px;top:190px;width:196px;font-size:10.2px;line-height:15px;color:var(--muted)}

/* clients */
.clients{position:absolute;left:0;top:1249px;width:1200px;height:238px;background:var(--blue)}
.clients .section-title{color:#fff;top:42px}
.client{position:absolute;top:104px;width:150px;height:80px;background:#fff;display:flex;align-items:center;justify-content:center;gap:7px;font-family:"Outfit",sans-serif;font-weight:500;font-size:18px;color:var(--ink)}
.client i{width:14px;height:14px;border-radius:50%;background:var(--blue);display:block}

/* work */
.work{position:absolute;top:1604px;width:249px;height:350px;background:#fff;box-shadow:0 2px 8px rgba(20,25,60,.1);border-bottom:3px solid var(--green)}
.work .pic{width:249px;height:156px}
.work h3{position:absolute;left:18px;top:173px;width:220px;font-family:"Outfit",sans-serif;font-weight:500;font-size:13.5px;line-height:19px;color:var(--ink)}
.work hr{position:absolute;left:18px;top:225px;width:212px;border:0;border-top:1px dashed var(--line)}
.work p{position:absolute;left:18px;top:236px;width:215px;font-size:10.2px;line-height:15px;color:var(--muted)}
.work .client-name{position:absolute;left:18px;top:298px;display:flex;align-items:center;gap:6px;font-family:"Outfit",sans-serif;font-weight:400;font-size:25px;color:#3a3a3a}
.work .client-name i{display:block;width:18px;height:18px;border-radius:50%;background:#8a8a8a}

/* contact band */
.cta{position:absolute;left:0;top:2075px;width:1200px;height:367px}
.cta-copy{position:absolute;top:204px;width:600px;text-align:center;color:#fff}
.cta-copy strong{display:block;font-family:"Outfit",sans-serif;font-weight:600;font-size:19px;letter-spacing:.5px;line-height:24px}
.cta-copy span{display:block;font-family:"Outfit",sans-serif;font-weight:400;font-size:19px;line-height:24px}
.subscribe{position:absolute;left:712px;top:2344px;width:375px;height:31px;display:flex;border-radius:16px;overflow:hidden;background:#fff}
.subscribe .field{flex:1;padding-left:18px;font-size:10px;line-height:31px;color:#333}
.subscribe .send{width:88px;background:var(--blue);color:#fff;font-size:9.5px;font-weight:700;text-align:center;line-height:31px}

/* footer */
.site-footer{position:absolute;left:0;top:2442px;width:1200px;height:312px;background:var(--footer)}
.site-footer .brand{left:200px;top:63px;color:var(--ink);font-size:20px}
.socials{position:absolute;left:200px;top:109px;display:flex;gap:7px}
.socials span{width:25px;height:25px;border-radius:50%;background:var(--blue);display:block}
.socials span.hl{background:var(--green)}
.foot-h{position:absolute;top:59px;font-family:"Outfit",sans-serif;font-weight:500;font-size:16px;color:var(--ink)}
.contact-list{position:absolute;left:549px;top:93px;font-size:10.5px;color:var(--ink)}
.contact-list .row{position:relative;padding-left:24px;margin-bottom:7px;line-height:15px}
.contact-list .row svg{position:absolute;left:0;top:1px}
.contact-list .phone{font-size:13px;font-family:"Outfit",sans-serif}
.contact-list .addr{margin-top:13px}
.quick-links{position:absolute;left:850px;top:92px;list-style:none}
.quick-links li{font-size:10.5px;line-height:19px;color:var(--ink)}
.foot-rule{position:absolute;left:200px;top:248px;width:800px;border-top:1px solid var(--line)}
.copyright{position:absolute;left:0;top:272px;width:1200px;text-align:center;font-size:9.5px;color:var(--ink)}
.copyright b{color:var(--blue);font-weight:500}
</style>
</head>
<body>
<div class="page">

  <section class="hero">
    <div class="hero-photo" role="img" aria-label="Photo of a person writing in a notebook beside a laptop"></div>
    <svg class="hero-wave" width="1200" height="668" viewBox="0 0 1200 668" aria-hidden="true">
      <path fill="var(--green)" d="M0,588 C90,528 220,480 320,535 C420,590 560,690 690,648 C800,610 860,690 1000,662 C1100,642 1160,620 1200,600 L1200,668 L0,668 Z"/>
      <path fill="#fff" d="M0,600 C120,566 260,560 390,612 C450,636 490,548 560,550 C640,553 650,668 720,668 L0,668 Z"/>
      <path fill="#fff" d="M900,668 C980,665 1050,650 1120,638 C1160,630 1185,630 1200,628 L1200,668 Z"/>
    </svg>
    <h1 class="hero-title">Communication Your<br>Expertise and Your Customer<br>Successes</h1>
    <a class="btn btn-green" style="left:94px;top:367px;width:125px;height:31px">CONTACT US</a>
    <div class="hero-dots"><span></span><span class="on"></span><span></span><span></span></div>
  </section>

  <header class="site-header">
    <div class="brand-panel"></div>
    <div class="brand">Lanternfield Prose <span class="u">Studio</span></div>
    <nav class="nav">
      <a class="active" style="left:591px">HOME</a>
      <a style="left:653px">OUR WORK</a>
      <a style="left:742px">CAPABILITIES</a>
      <a style="left:840px">ABOUT US</a>
      <a style="left:922px">BLOG</a>
    </nav>
    <a class="btn btn-blue" style="left:981px;top:16px;width:125px;height:31px">GET IN TOUCH</a>
  </header>

  <h2 class="section-title" style="top:710px">Text copy that explains in concise, snappy terms<br>the value you provide to customers.</h2>

  <article class="service" style="left:94px">
    <div class="pic" role="img" aria-label="Photo of a team planning around a desk with charts" style="background:linear-gradient(135deg,#8a8f94,#c9cdd0 60%,#6d7378)"></div>
    <div class="tag" style="background:var(--blue)">Strategy</div>
    <p>At vero eos et accusamus et iusto odio dignissimos ducimus qui blanditi-is praesentium voluptatum deleniti atque corrupti quos dolores et quas molestias excepturi sint occaecati cu-piditate non provident, similique sunt in culpa qui officia deserunt.</p>
  </article>
  <article class="service" style="left:353px">
    <div class="pic" role="img" aria-label="Photo of a coach presenting to a small group" style="background:linear-gradient(135deg,#d6d8d9,#9a9ea2 55%,#3c3f44)"></div>
    <div class="tag" style="background:var(--green)">Coaching</div>
    <p>At vero eos et accusamus et iusto odio dignissimos ducimus qui blanditi-is praesentium voluptatum deleniti atque corrupti quos dolores et quas molestias excepturi sint occaecati cu-piditate non provident, similique sunt in culpa qui officia deserunt.</p>
  </article>
  <article class="service" style="left:612px">
    <div class="pic" role="img" aria-label="Photo of hands typing on a laptop keyboard" style="background:linear-gradient(135deg,#c8c4bf,#8e8a86 55%,#4d4b4a)"></div>
    <div class="tag" style="background:var(--blue-dark)">Writing</div>
    <p>At vero eos et accusamus et iusto odio dignissimos ducimus qui blanditi-is praesentium voluptatum deleniti atque corrupti quos dolores et quas molestias excepturi sint occaecati cu-piditate non provident, similique sunt in culpa qui officia deserunt.</p>
  </article>
  <article class="service" style="left:872px">
    <div class="pic" role="img" aria-label="Photo of an editor reviewing notes at a desk" style="background:linear-gradient(135deg,#e3e6e8,#b9c1c6 55%,#7b8a92)"></div>
    <div class="tag" style="background:var(--blue-light)">Editing</div>
    <p>At vero eos et accusamus et iusto odio dignissimos ducimus qui blanditi-is praesentium voluptatum deleniti atque corrupti quos dolores et quas molestias excepturi sint occaecati cu-piditate non provident, similique sunt in culpa qui officia deserunt.</p>
  </article>

  <a class="btn btn-blue" style="left:525px;top:1155px;width:150px;height:32px">VIEW OUR CAPABILITIES</a>

  <section class="clients">
    <h2 class="section-title">View our past and current clients</h2>
    <div class="client" style="left:200px">Northvale</div>
    <div class="client" style="left:363px">Brightmoor</div>
    <div class="client" style="left:525px"><i></i>Corvelle</div>
    <div class="client" style="left:688px;font-size:16px">Pinecrest Labs</div>
    <div class="client" style="left:850px"><i></i>Tessaline</div>
  </section>

  <h2 class="section-title" style="top:1541px">Work we have done</h2>

  <article class="work" style="left:200px">
    <div class="pic" role="img" aria-label="Photo of a hand writing in a notebook next to a laptop" style="background:linear-gradient(135deg,#2d5a7a,#6d93ad 55%,#5a4a3c)"></div>
    <h3>There are many variations lorem Ipsum available, literature</h3>
    <hr>
    <p>Lorem ipsum dolor sit amet, consectetur adipiscing elit, sed do eiusmod tempor incididunt ut labore</p>
    <div class="client-name"><i></i>Corvelle</div>
  </article>
  <article class="work" style="left:475px">
    <div class="pic" role="img" aria-label="Photo of colleagues reviewing printed reports" style="background:linear-gradient(135deg,#c7cbd0,#8d949b 55%,#3d4248)"></div>
    <h3>There are many variations lorem Ipsum available, literature</h3>
    <hr>
    <p>Lorem ipsum dolor sit amet, consectetur adipiscing elit, sed do eiusmod tempor incididunt ut labore</p>
    <div class="client-name"><i></i>Corvelle</div>
  </article>
  <article class="work" style="left:750px">
    <div class="pic" role="img" aria-label="Photo of a team meeting around computer screens" style="background:linear-gradient(135deg,#d9d6d2,#9b948d 55%,#3e3934)"></div>
    <h3>There are many variations lorem Ipsum available, literature</h3>
    <hr>
    <p>Lorem ipsum dolor sit amet, consectetur adipiscing elit, sed do eiusmod tempor incididunt ut labore</p>
    <div class="client-name"><i></i>Corvelle</div>
  </article>

  <a class="btn btn-green" style="left:537px;top:1986px;width:126px;height:31px">VIEW OUR WORK</a>

  <section class="cta">
    <svg width="1200" height="367" viewBox="0 0 1200 367" aria-hidden="true" style="position:absolute;left:0;top:0">
      <defs>
        <linearGradient id="split" x1="0" y1="0" x2="1" y2="0">
          <stop offset="0.5" stop-color="var(--slate)"/>
          <stop offset="0.5" stop-color="var(--steel)"/>
        </linearGradient>
      </defs>
      <path fill="var(--green)" d="M0,68 C70,30 150,4 230,6 C300,8 330,40 390,55 C450,70 480,5 530,0 C580,-4 620,60 700,120 C760,70 800,40 880,40 C960,40 1000,90 1060,80 C1120,70 1170,40 1200,22 L1200,367 L0,367 Z"/>
      <path fill="url(#split)" d="M0,118 C80,60 160,2 240,2 C300,2 340,65 400,70 C470,76 500,60 560,85 C620,110 660,140 720,150 C790,162 840,175 900,180 C980,186 1040,150 1110,120 C1150,105 1180,98 1200,95 L1200,367 L0,367 Z"/>
    </svg>
    <div class="cta-copy" style="left:0"><strong>FEEL FREE TO CONTACT US</strong><span>with any quastions. we're happy to help.</span></div>
    <div class="cta-copy" style="left:600px"><strong>EDITORIAL INSPIRATION</strong><span>delivered straight to your inbox.</span></div>
  </section>
  <a class="btn btn-green" style="left:237px;top:2344px;width:126px;height:31px">GET IN TOUCH</a>
  <form class="subscribe"><div class="field">Enter your email ...</div><div class="send">SUBMIT</div></form>

  <footer class="site-footer">
    <div class="brand">Lanternfield Prose <span class="u">Studio</span></div>
    <div class="socials"><span></span><span></span><span class="hl"></span><span></span></div>

    <h4 class="foot-h" style="left:549px">Contact Us</h4>
    <div class="contact-list">
      <div class="row phone"><svg width="13" height="13" viewBox="0 0 24 24"><path fill="none" stroke="var(--blue)" stroke-width="2" d="M5 3h4l2 5-3 2a12 12 0 0 0 6 6l2-3 5 2v4a2 2 0 0 1-2 2A18 18 0 0 1 3 5a2 2 0 0 1 2-2z"/></svg>(555) 014-2298</div>
      <div class="row"><svg width="12" height="12" viewBox="0 0 24 24"><rect x="2" y="5" width="20" height="14" rx="2" fill="none" stroke="var(--blue)" stroke-width="2"/><path d="M2 6l10 7 10-7" fill="none" stroke="var(--blue)" stroke-width="2"/></svg>info@lpstudio.net</div>
      <div class="row addr"><svg width="11" height="12" viewBox="0 0 24 24"><path d="M12 2a7 7 0 0 0-7 7c0 5 7 13 7 13s7-8 7-13a7 7 0 0 0-7-7z" fill="none" stroke="var(--blue)" stroke-width="2"/><circle cx="12" cy="9" r="2.5" fill="var(--blue)"/></svg>Harbor Row Commons,<br>2870 Quill Ave NE., # 118, Marlow<br>Bay - 60417</div>
    </div>

    <h4 class="foot-h" style="left:850px">Quick Links</h4>
    <ul class="quick-links">
      <li>Home</li><li>Our Work</li><li>Capabilities</li><li>About Us</li><li>Blog</li><li>Contact Us</li>
    </ul>

    <div class="foot-rule"></div>
    <p class="copyright">© 2021 <b>Lanternfield Prose Studio.</b> All Right Reserved</p>
  </footer>

</div>
</body>
</html>
```